WordPress Website for Pain Relief Clinic

I need a WordPress website designed for my laser pain relief clinic. It needs to be a professional, responsive design with 7 pages: Home, Why Choose Us, Treatable Conditions, Testimonials, FAQ, Franchising, Contact Us. Here is logo: https://files.brivoltcdn.com/media.t-w-e-n.com/sitebuilder/472/CalvexaLogoHighQuality.png

Target Market(s)

people with pain,elderly adults,injuries,soreness

Industry/Entity Type

Clinic

Number of Pages Required

5+ page

Colors
0792cd
85abd2

```html
<!DOCTYPE html>
<html lang="en">
<head>
<meta charset="utf-8">
<title>Calvexa Laser Pain Relief Clinic</title>
<link href="https://fonts.googleapis.com/css2?family=Open+Sans:wght@400;600;700;800&family=Raleway:wght@400;600;700;800&display=swap" rel="stylesheet">
<style>
:root{
  --blue:#0792cd;
  --blue-soft:#85abd2;
  --blue-dark:#05679a;
  --red:#e0262a;
  --ink:#222;
  --text:#666;
  --line:#e2e2e2;
  --nav:#1d1d1d;
  --green:#7cb342;
  --teal:#26a69a;
  --footer:#f3f3f3;
}
*{box-sizing:border-box;margin:0;padding:0}
html,body{width:1200px;height:2868px;overflow:hidden}
body{font-family:"Open Sans",Arial,sans-serif;color:var(--text);background:#fff;position:relative}
.abs{position:absolute}
h2,h3,h4{font-family:"Raleway",Arial,sans-serif;color:var(--ink)}
p{font-size:13px;line-height:21px}

/* header */
.header{top:0;left:0;width:1200px;height:92px;background:#fff}
.brand{left:40px;top:18px;display:flex;align-items:center;gap:12px}
.brand-mark{width:48px;height:48px;border-radius:50%;background:var(--blue)}
.brand-name{font-size:34px;font-weight:700;color:var(--blue);line-height:1}
.brand-sub{left:100px;top:58px;font-size:11px;letter-spacing:2px;color:#888;text-transform:uppercase}
.contact-mail{left:640px;top:14px;font-size:12px;color:#555;line-height:17px}
.contact-mail b{color:var(--ink)}
.socials{left:1040px;top:10px;display:flex;gap:10px}
.socials span{width:22px;height:22px;border-radius:50%;background:#9aa3ad;display:block}
.call{left:820px;top:46px;display:flex;align-items:center}
.call-label{background:var(--blue);color:#fff;font-size:13px;font-weight:700;padding:9px 16px;display:flex;gap:8px;align-items:center}
.call-number{background:var(--red);color:#fff;font-size:22px;font-weight:800;padding:4px 16px;line-height:27px}

/* nav */
.nav{top:92px;left:0;width:1200px;height:34px;background:var(--nav);display:flex;align-items:center}
.nav a{color:#ddd;text-decoration:none;font-size:11px;font-weight:700;padding:0 16px;line-height:34px;text-transform:uppercase}
.nav a.active{background:var(--red);color:#fff;margin-left:40px}
.search{right:40px;top:8px;width:150px;height:19px;background:#fff;font-size:10px;color:#999;padding:2px 8px}

/* hero */
.hero{top:126px;left:0;width:1200px;height:580px;background:linear-gradient(115deg,#c6ced3 0%,#d8b8a6 45%,#b98e78 65%,#5b6a75 100%)}
.hero-card{left:40px;width:240px;height:118px;padding:18px 16px 0 74px;color:#fff}
.hero-card .ico{position:absolute;left:16px;top:20px;width:44px;height:44px;border:2px solid #fff;border-radius:50%;display:flex;align-items:center;justify-content:center}
.hero-card h4{color:#fff;font-size:15px;margin-bottom:6px}
.hero-card p{font-size:10px;line-height:14px;color:#f2f2f2}
.c1{top:20px;background:rgba(124,179,66,.92)}
.c2{top:146px;background:rgba(7,146,205,.92)}
.c3{top:272px;background:rgba(224,38,42,.9)}
.c4{top:398px;background:rgba(38,166,154,.92)}
.hero-copy{left:640px;top:270px;width:520px}
.hero-copy .small{font-size:22px;color:#fff;font-family:"Raleway",sans-serif;font-weight:600}
.hero-copy .big{font-size:46px;color:#fff;font-family:"Raleway",sans-serif;font-weight:800;line-height:52px}
.hero-copy p{color:#fff;font-size:12px;line-height:18px;margin:10px 0 16px}
.btn-dark{background:#111;color:#fff;font-size:11px;font-weight:700;padding:9px 18px;display:inline-block;text-transform:uppercase}
.dots{left:1080px;top:540px;display:flex;gap:6px}
.dots span{width:8px;height:8px;border-radius:50%;background:#fff;opacity:.6}
.dots span.on{opacity:1;background:var(--red)}

/* welcome */
.welcome{left:40px;top:740px;width:680px}
.welcome h2{font-size:30px;font-weight:800;color:var(--ink)}
.welcome h2 span{color:var(--blue)}
.welcome .tag{font-size:13px;color:#888;font-style:italic;margin:2px 0 16px}
.welcome p{margin-bottom:14px}
.btn-blue{background:var(--blue);color:#fff;font-size:11px;font-weight:700;padding:9px 16px;display:inline-block;text-transform:uppercase}

.booking{left:800px;top:740px;width:360px;height:420px;background:#f5f5f5;border:1px solid var(--line)}
.booking-head{background:var(--blue);color:#fff;padding:12px 18px}
.booking-head h3{color:#fff;font-size:20px;font-weight:800;text-transform:uppercase}
.booking-head div{font-size:14px;margin-top:4px;font-weight:600}
.field{margin:10px 18px 0;height:28px;background:#fff;border:1px solid #ddd;font-size:11px;color:#aaa;padding:6px 10px}
.field.msg{height:66px}
.captcha{margin:10px 18px 0;display:flex;gap:10px}
.captcha .field{margin:0;width:150px}
.captcha .code{width:90px;height:28px;background:#e6e6e6;font-style:italic;color:#555;font-size:13px;padding:5px 10px}
.booking .btn-blue{margin:12px 18px 0}

/* why choose */
.why{left:40px;top:1240px;width:1120px}
.why h2{font-size:30px;font-weight:400;color:#333;border-bottom:1px solid var(--line);padding-bottom:12px}
.why h2 b{font-weight:800;color:var(--ink)}
.why-cols{display:flex;gap:40px;margin-top:24px}
.why-item{flex:1;display:flex;gap:14px}
.why-item .num{font-family:"Raleway",sans-serif;font-size:40px;font-weight:800;color:#cfcfcf;line-height:40px}
.why-item h4{font-size:14px;margin-bottom:4px}
.why-item p{font-size:12px;line-height:18px}

/* services */
.services{top:1440px;left:0;width:1200px;height:560px;background:linear-gradient(180deg,#3d444a,#2a2f34)}
.services h2{position:absolute;top:46px;width:1200px;text-align:center;color:#fff;font-size:28px;font-weight:400}
.services h2 b{font-weight:800}
.services .rule{position:absolute;top:90px;left:560px;width:80px;height:3px;background:var(--blue)}
.svc{top:150px;width:240px;height:340px;background:#fff}
.svc .ph{height:170px}
.svc h4{font-size:14px;margin:14px 14px 6px;text-transform:uppercase}
.svc p{font-size:11px;line-height:16px;margin:0 14px 12px}
.svc .btn-blue{margin-left:14px;font-size:10px;padding:6px 12px}
.arrow{top:300px;width:30px;height:30px;border:2px solid #fff;border-radius:50%;display:flex;align-items:center;justify-content:center}

/* doctor */
.doctor{left:40px;top:2040px;width:360px}
.doctor h3{font-size:22px;font-weight:800;text-transform:uppercase}
.doctor .role{font-size:11px;color:#999;margin:2px 0 18px}
.doctor p{margin-bottom:14px}
.doc-photo{left:420px;top:2020px;width:330px;height:420px;background:radial-gradient(ellipse at 50% 30%,#eef3f6 0%,#cfdbe3 55%,#8fb1c8 100%)}
.reviews{left:790px;top:2030px;width:370px}
.reviews h2{font-size:28px;font-weight:400;border-bottom:1px solid var(--line);padding-bottom:12px}
.reviews h2 b{font-weight:800}
.quote{margin-top:22px;background:#f4f4f4;padding:22px;border-left:4px solid var(--blue)}
.quote p{font-size:12px;line-height:19px}
.quote .who{text-align:right;font-style:italic;margin-top:10px;font-size:12px;color:#555}

/* newsletter */
.news{top:2470px;left:0;width:1200px;height:90px;background:var(--blue);display:flex;align-items:center;padding:0 40px}
.news .ico{width:44px;height:44px;border-radius:50%;border:2px solid #fff;display:flex;align-items:center;justify-content:center}
.news h4{color:#fff;font-size:17px;font-weight:800;margin-left:14px;line-height:20px;text-transform:uppercase;width:160px}
.news .input{margin-left:60px;width:300px;height:32px;background:#fff;font-size:11px;color:#999;padding:8px 12px}
.news .sub{background:var(--blue-dark);color:#fff;font-size:11px;font-weight:700;padding:9px 18px;margin-left:4px}
.news .stay{margin-left:110px;color:#fff;font-family:"Raleway",sans-serif;font-weight:800;font-size:17px;line-height:20px}
.news .socials{position:static;margin-left:20px}
.news .socials span{background:rgba(255,255,255,.85);width:26px;height:26px}

/* footer */
.footer{top:2560px;left:0;width:1200px;height:308px;background:var(--footer)}
.fcol{top:30px}
.fcol h4{font-size:14px;font-weight:800;text-transform:uppercase;border-bottom:1px solid #ddd;padding-bottom:8px;margin-bottom:12px}
.fcol p{font-size:11px;line-height:17px}
.fcol .date{color:var(--blue);font-size:10px;font-weight:700}
.frow{display:flex;gap:10px;margin-bottom:12px;align-items:flex-start}
.fico{width:24px;height:24px;border-radius:50%;background:var(--blue);flex:none;display:flex;align-items:center;justify-content:center}
.flogo{left:880px;top:40px;display:flex;align-items:center;gap:10px}
.flogo .brand-mark{width:40px;height:40px}
.flogo .brand-name{font-size:30px}
.fcopy{left:880px;top:110px;width:280px;font-size:10px;line-height:15px;color:#888}
</style>
</head>
<body>

<header class="abs header">
  <div class="abs brand"><span class="brand-mark"></span><span class="brand-name">Calvexa</span></div>
  <div class="abs brand-sub">Laser Pain Relief Clinic</div>
  <div class="abs contact-mail"><b>EMAIL</b><br>info@calvexapainrelief.com</div>
  <div class="abs socials"><span></span><span></span><span></span></div>
  <div class="abs call">
    <div class="call-label">
      <svg width="14" height="14" viewBox="0 0 24 24"><path fill="#fff" d="M6.6 10.8a15 15 0 0 0 6.6 6.6l2.2-2.2c.3-.3.7-.4 1-.2 1.1.4 2.3.6 3.6.6.6 0 1 .4 1 1V20c0 .6-.4 1-1 1A17 17 0 0 1 3 4c0-.6.4-1 1-1h3.5c.6 0 1 .4 1 1 0 1.3.2 2.5.6 3.6.1.3 0 .7-.2 1z"/></svg>
      CALL US TODAY NOW!
    </div>
    <div class="call-number">248-555-0142</div>
  </div>
</header>

<nav class="abs nav">
  <a class="active">Home</a><a>Why Choose Us</a><a>Treatable Conditions</a><a>Testimonials</a><a>FAQ</a><a>Franchising</a><a>Contact</a>
  <div class="abs search">Search here</div>
</nav>

<section class="abs hero" role="img" aria-label="Photo of a person holding a painful knee, warm skin tones on a soft grey background">
  <div class="abs hero-card c1"><span class="ico"><svg width="22" height="22" viewBox="0 0 24 24" fill="none" stroke="#fff" stroke-width="2"><rect x="3" y="5" width="18" height="16"/><path d="M3 10h18M8 3v4M16 3v4"/></svg></span><h4>Schedule an Appointment</h4><p>Book a visit with our laser team in a few quick steps today.</p></div>
  <div class="abs hero-card c2"><span class="ico"><svg width="22" height="22" viewBox="0 0 24 24" fill="none" stroke="#fff" stroke-width="2"><path d="M3 21V9l9-6 9 6v12H3zM9 21v-7h6v7"/></svg></span><h4>Our Franchising</h4><p>Open a clinic in your city and join our growing network.</p></div>
  <div class="abs hero-card c3"><span class="ico"><svg width="22" height="22" viewBox="0 0 24 24" fill="none" stroke="#fff" stroke-width="2"><circle cx="12" cy="12" r="9"/><path d="M9.5 9a2.5 2.5 0 1 1 3 2.5c-.5.2-.5.8-.5 1.5M12 17v.5"/></svg></span><h4>What can you Expect?</h4><p>Gentle, drug free sessions with no downtime at all.</p></div>
  <div class="abs hero-card c4"><span class="ico"><svg width="22" height="22" viewBox="0 0 24 24" fill="none" stroke="#fff" stroke-width="2"><circle cx="12" cy="8" r="4"/><path d="M4 21c1-4 4-6 8-6s7 2 8 6"/></svg></span><h4>Meet the Doctor</h4><p>Learn about the specialist who leads every treatment plan.</p></div>
  <div class="abs hero-copy">
    <div class="small">WANT RELIEF FROM</div>
    <div class="big">KNEE-PAIN? TELL US</div>
    <p>Our laser therapy targets the source of knee pain, easing swelling and stiffness so you can move freely again.</p>
    <span class="btn-dark">Book an Appointment</span>
  </div>
  <div class="abs dots"><span class="on"></span><span></span><span></span><span></span></div>
</section>

<section class="abs welcome">
  <h2>WELCOME TO <span>CALVEXA</span></h2>
  <div class="tag">Laser Pain Relief Clinic</div>
  <p>Our clinic uses advanced laser therapy to relieve chronic and acute pain without drugs or surgery. Each visit is short, comfortable and tailored to your needs, with a care plan that follows your progress week by week and helps you return to daily life.</p>
  <p>We treat adults of every age, from athletes with fresh injuries to seniors with long lasting joint soreness. Our staff explain every step, answer your questions and make sure you feel at ease from the moment you arrive until you leave our clinic.</p>
  <p>Laser light reaches deep into tissue, speeding natural healing and calming inflammation. Many patients feel lighter after their first sessions and keep improving over the following weeks.</p>
  <span class="btn-blue">Read More</span>
</section>

<aside class="abs booking">
  <div class="booking-head"><h3>Book an Appointment</h3><div>&#9742; 248-555-0142</div></div>
  <div class="field">Full Name</div>
  <div class="field">Phone Number</div>
  <div class="field">Email Address</div>
  <div class="field">Select Date</div>
  <div class="field msg">Message</div>
  <div class="captcha"><div class="field">Enter Code</div><div class="code">m7x4a</div></div>
  <span class="btn-blue">Submit Request</span>
</aside>

<section class="abs why">
  <h2><b>WHY</b> CHOOSE US</h2>
  <div class="why-cols">
    <div class="why-item"><span class="num">01</span><div><h4>Proven Laser Care</h4><p>Safe treatments backed by years of results with thousands of patients.</p></div></div>
    <div class="why-item"><span class="num">02</span><div><h4>No Drugs Needed</h4><p>Relief that works with your body, free of pills and their side effects.</p></div></div>
    <div class="why-item"><span class="num">03</span><div><h4>Friendly Expert Team</h4><p>Caring staff who guide you through every session with full attention.</p></div></div>
  </div>
</section>

<section class="abs services">
  <h2>WE OFFER <b>RELIABLE SERVICES</b></h2>
  <div class="rule"></div>
  <div class="abs arrow" style="left:40px"><svg width="12" height="12" viewBox="0 0 12 12"><path d="M8 1L3 6l5 5" stroke="#fff" stroke-width="2" fill="none"/></svg></div>
  <div class="abs arrow" style="left:1130px"><svg width="12" height="12" viewBox="0 0 12 12"><path d="M4 1l5 5-5 5" stroke="#fff" stroke-width="2" fill="none"/></svg></div>
  <div class="abs svc" style="left:90px"><div class="ph" role="img" aria-label="Photo of a lower back with red pain area" style="background:linear-gradient(135deg,#e7c1a8,#b5765a)"></div><h4>Back Pain</h4><p>Ease tight muscles and sore discs with focused laser sessions.</p><span class="btn-blue">Read More</span></div>
  <div class="abs svc" style="left:360px"><div class="ph" role="img" aria-label="Photo of hands holding an aching knee" style="background:linear-gradient(135deg,#f0d2bf,#c48a6c)"></div><h4>Knee Pain</h4><p>Reduce swelling and stiffness to walk and climb with ease.</p><span class="btn-blue">Read More</span></div>
  <div class="abs svc" style="left:630px"><div class="ph" role="img" aria-label="Photo of a bare shoulder with pain highlight" style="background:linear-gradient(135deg,#e9c6ae,#a8684c)"></div><h4>Shoulder Pain</h4><p>Restore motion in stiff, injured or overused shoulders.</p><span class="btn-blue">Read More</span></div>
  <div class="abs svc" style="left:900px"><div class="ph" role="img" aria-label="Photo of a forearm and elbow with pain area" style="background:linear-gradient(135deg,#efd0ba,#b97b60)"></div><h4>Arm Pain</h4><p>Calm elbow, wrist and forearm strain from daily tasks.</p><span class="btn-blue">Read More</span></div>
</section>

<section class="abs doctor">
  <h3>Dr. Alan Morrow</h3>
  <div class="role">MD, Calvexa Laser Pain Relief Clinic</div>
  <p>Dr. Morrow has spent many years helping patients find lasting relief from pain. He combines modern laser therapy with careful assessment to create plans that fit each person and their goals.</p>
  <p>He believes in clear talk, honest advice and steady follow up, so every patient knows what to expect and feels supported at each stage of recovery.</p>
</section>
<div class="abs doc-photo" role="img" aria-label="Photo of the clinic doctor in a white coat with a stethoscope"></div>

<section class="abs reviews">
  <h2><b>WHAT OUR</b> PATIENTS SAY</h2>
  <div class="quote">
    <p>After months of knee pain I could barely walk my dog. A few laser sessions later I am back on my morning walks. The team was kind, patient and explained everything clearly. I recommend this clinic to anyone tired of living with daily pain.</p>
    <div class="who">- Grace Holden</div>
  </div>
</section>

<section class="abs news">
  <span class="ico"><svg width="22" height="22" viewBox="0 0 24 24" fill="none" stroke="#fff" stroke-width="2"><rect x="3" y="6" width="18" height="13"/><path d="M3 7l9 6 9-6"/></svg></span>
  <h4>Subscribe our Newsletter</h4>
  <div class="input">Enter Email</div>
  <span class="sub">SUBSCRIBE</span>
  <div class="stay">STAY<br>CONNECTED</div>
  <div class="socials"><span></span><span></span><span></span><span></span></div>
</section>

<footer class="abs footer">
  <div class="abs fcol" style="left:40px;width:240px">
    <h4>Recent Blog</h4>
    <div class="date">10 JAN 2015</div><p style="margin-bottom:12px">How laser light helps sore joints heal faster.</p>
    <div class="date">15 JAN 2015</div><p>Simple habits to protect your back at work.</p>
  </div>
  <div class="abs fcol" style="left:320px;width:220px">
    <h4>Office Hours</h4>
    <p><b>Monday to Friday</b><br>9:00am - 7:00pm</p>
    <p style="margin-top:10px"><b>Saturday</b><br>9:00am - 2:00pm</p>
    <p style="margin-top:10px"><b>Sunday</b><br>Closed</p>
  </div>
  <div class="abs fcol" style="left:580px;width:260px">
    <h4>Get in Touch</h4>
    <div class="frow"><span class="fico"><svg width="12" height="12" viewBox="0 0 24 24"><path fill="#fff" d="M12 2a7 7 0 0 0-7 7c0 5 7 13 7 13s7-8 7-13a7 7 0 0 0-7-7zm0 9.5A2.5 2.5 0 1 1 12 6.5a2.5 2.5 0 0 1 0 5z"/></svg></span><p>1240 Maple Ridge Drive, Suite 8<br>Brookfield, MI 48077</p></div>
    <div class="frow"><span class="fico"><svg width="12" height="12" viewBox="0 0 24 24"><path fill="#fff" d="M6.6 10.8a15 15 0 0 0 6.6 6.6l2.2-2.2c.3-.3.7-.4 1-.2 1.1.4 2.3.6 3.6.6.6 0 1 .4 1 1V20c0 .6-.4 1-1 1A17 17 0 0 1 3 4c0-.6.4-1 1-1h3.5c.6 0 1 .4 1 1 0 1.3.2 2.5.6 3.6.1.3 0 .7-.2 1z"/></svg></span><p>Phone<br>248-555-0142</p></div>
    <div class="frow"><span class="fico"><svg width="12" height="12" viewBox="0 0 24 24"><path fill="#fff" d="M3 6h18v12H3zm1 1 8 6 8-6"/></svg></span><p>Email<br>info@calvexapainrelief.com</p></div>
  </div>
  <div class="abs flogo"><span class="brand-mark"></span><span class="brand-name">Calvexa</span></div>
  <div class="abs fcopy">&copy; 2015 Calvexa Laser Pain Relief Clinic. All Rights Reserved. Terms &amp; Conditions | Privacy Policy</div>
</footer>

</body>
</html>
```